Law Firm St. Patrick's Day Party

Two different law firm's joining to have a St. Patrick's Day party. Invitees will include other lawyers, clients and friends. This is intended to be more of a causal event. So we are looking for an invite that is fun but not cheesy.

The invite will be a two sided "post card." One side should be the details of event and design. The opposite side should be our firm logos (see uploads) with an area on the right side for postage and mailing address. We will be providing live music, food and drinks. Also...the NVBL Basketball Tournaments will playing the same day...some sort of reference that we Will have TVs to watch the Basketball games is needed too.

Target Market(s)

Fun professional crowd

Industry/Entity Type

Law Firm

Font styles to use
Serif
Decorative
Script

Requirements
Must have
• time, date and where...food, drinks TVs (NVBL games)
• Essential Information: Friday, March 17th. The party will start at 2:00 p.m. and run until "Whenever." The location of the Party is 2846 Birch Lane, Kansas City, Missouri 64108.
Nice to have
• something festive for St. Pat's day

```html
<!DOCTYPE html>
<html lang="en">
<head>
<meta charset="utf-8">
<title>Joint St. Patrick's Day Party Invitation</title>
<link href="https://fonts.googleapis.com/css2?family=Lobster&family=Open+Sans:wght@400;600;700&family=Libre+Baskerville:ital@0;1&display=swap" rel="stylesheet">
<style>
  :root {
    --backdrop: #e9dcc6;
    --green-deep: #2b5a1f;
    --green-mid: #3f7f22;
    --green-bright: #6fbf2a;
    --cream: #ece4d3;
    --cream-edge: #d8ccb4;
    --orange: #e8731c;
    --ink: #1d1d1d;
    --gold: #a8925c;
    --blue: #3d74ee;
    --blue-text: #2c58b8;
    --white: #ffffff;
    --stamp: #8aa0a8;
  }
  * { box-sizing: border-box; margin: 0; padding: 0; }
  html, body { width: 1200px; height: 471px; overflow: hidden; background: var(--backdrop); }
  .canvas { position: relative; width: 1200px; height: 471px; }

  /* Front side */
  .card-front {
    position: absolute; left: 57px; top: 57px; width: 515px; height: 358px;
    background: radial-gradient(ellipse at center, var(--green-bright) 0%, var(--green-mid) 45%, var(--green-deep) 100%);
  }
  .invite-panel {
    position: absolute; left: 66px; top: 13px; width: 384px; height: 328px;
    background: var(--cream); border: 2px solid var(--cream-edge); border-radius: 14px;
  }
  .invite-panel > * { position: absolute; left: 0; right: 0; text-align: center; }
  .invite-heading {
    top: 5px; font-family: "Lobster", cursive; font-weight: 400; color: var(--green-deep);
    font-size: 19px; line-height: 23px;
  }
  .shamrock-ornament {
    top: 81px; left: 156px; right: auto; width: 68px; height: 20px; border-radius: 10px; background: var(--green-bright);
  }
  .event-day { top: 106px; font-family: "Open Sans", sans-serif; font-weight: 700; color: var(--orange); font-size: 17px; line-height: 22px; }
  .date-banner { top: 129px; left: 152px; right: auto; }
  .flourish { top: 142px; width: 42px; height: 58px; border-radius: 20px; background: #c9cfb3; right: auto; }
  .flourish-left { left: 113px; }
  .flourish-right { left: 233px; }
  .event-time { top: 236px; font-family: "Open Sans", sans-serif; font-weight: 700; font-size: 14px; line-height: 18px; color: var(--ink); }
  .event-address { top: 256px; font-family: "Open Sans", sans-serif; font-size: 11.5px; line-height: 12.5px; color: var(--orange); }
  .event-perks {
    top: 299px; font-family: "Lobster", cursive; color: var(--orange); font-size: 15px; line-height: 20px;
  }
  .perk-dot { display: inline-block; width: 8px; height: 8px; border-radius: 50%; background: var(--green-mid); margin: 0 6px; vertical-align: middle; }

  /* Back side */
  .card-back { position: absolute; left: 628px; top: 57px; width: 515px; height: 358px; background: var(--white); overflow: hidden; }
  .rule-blue { position: absolute; left: 0; top: 8px; width: 515px; height: 6px; background: linear-gradient(90deg, var(--blue), rgba(61,116,238,0) 90%); }
  .rule-gold { position: absolute; left: 0; top: 282px; width: 515px; height: 5px; background: linear-gradient(90deg, rgba(168,146,92,0.1), var(--gold) 95%); }
  .stamp-box { position: absolute; left: 429px; top: 26px; width: 61px; height: 63px; border: 2px dashed var(--stamp); }
  .firm-name { position: absolute; display: flex; align-items: center; gap: 10px; font-family: "Libre Baskerville", serif; font-size: 19px; color: var(--ink); }
  .firm-mark { width: 34px; height: 34px; background: var(--gold); flex: none; }
  .firm-first { left: 32px; top: 40px; }
  .firm-second { left: 22px; top: 170px; color: var(--blue-text); }
  .firm-second .firm-mark { background: var(--blue); border-radius: 50%; }
  .contact-band { position: absolute; left: 0; width: 259px; height: 38px; color: var(--white); text-align: center; font-family: "Open Sans", sans-serif; }
  .contact-band .label { font-size: 9px; font-weight: 600; padding-top: 5px; letter-spacing: 0.3px; }
  .contact-band .phone { font-size: 13px; font-weight: 700; display: flex; justify-content: center; align-items: center; gap: 4px; }
  .band-gold { top: 100px; background: var(--gold); }
  .band-blue { top: 229px; background: var(--blue); }
  .barcode-label { position: absolute; left: 216px; top: 313px; font-family: "Open Sans", sans-serif; font-size: 10px; font-weight: 600; color: var(--ink); }
  .edge-tick { position: absolute; left: 505px; top: 306px; width: 10px; height: 1px; background: #d33; }
</style>
</head>
<body>
<div class="canvas">
  <section class="card-front">
    <div class="invite-panel">
      <h1 class="invite-heading">You are invited<br>to a joint<br>St. Patrick's Day Party</h1>
      <div class="shamrock-ornament" role="img" aria-label="Trio of green shamrocks"></div>
      <p class="event-day">Friday</p>
      <div class="flourish flourish-left" role="img" aria-label="Swirling shamrock vine ornament"></div>
      <svg class="date-banner" width="80" height="86" viewBox="0 0 80 86" aria-label="17 March 2017">
        <path d="M0 0 H80 V86 L40 72 L0 86 Z" fill="#2b5a1f"/>
        <path d="M4 4 H76 V79 L40 67 L4 79 Z" fill="none" stroke="#ffffff" stroke-width="1.2" stroke-dasharray="3 2"/>
        <text x="40" y="24" text-anchor="middle" font-family="Open Sans, sans-serif" font-weight="700" font-size="14" fill="#ffffff">17</text>
        <text x="40" y="42" text-anchor="middle" font-family="Open Sans, sans-serif" font-weight="700" font-size="14" fill="#ffffff">MARCH</text>
        <text x="40" y="60" text-anchor="middle" font-family="Open Sans, sans-serif" font-weight="700" font-size="14" fill="#ffffff">2017</text>
      </svg>
      <div class="flourish flourish-right" role="img" aria-label="Swirling shamrock vine ornament"></div>
      <p class="event-time">2:00 P.M. until "Whenever"</p>
      <p class="event-address">2846 Birch Lane,<br>Kansas City,<br>Missouri 64108</p>
      <p class="event-perks">Food<span class="perk-dot"></span>Drinks<span class="perk-dot"></span>TVs (NVBL Games)</p>
    </div>
  </section>

  <section class="card-back">
    <div class="rule-blue"></div>
    <div class="stamp-box"></div>
    <div class="firm-name firm-first"><span class="firm-mark"></span>Hollister &amp; Brandt LLC</div>
    <div class="contact-band band-gold">
      <p class="label">CALL FOR FREE CONSULTATION</p>
      <p class="phone">
        <svg width="12" height="12" viewBox="0 0 12 12"><circle cx="6" cy="6" r="5.2" fill="none" stroke="#fff" stroke-width="1"/><path d="M4 3.2 L5 4.6 L4.5 5.3 Q5.4 6.8 6.7 7.5 L7.4 7 L8.8 8 L8.2 8.9 Q5 8.6 3.2 4 Z" fill="#fff"/></svg>
        816.555.0142
      </p>
    </div>
    <div class="firm-name firm-second"><span class="firm-mark"></span>Marlowe Keene &amp; Ashby, LLC</div>
    <div class="contact-band band-blue">
      <p class="label">CONTACT US</p>
      <p class="phone">
        <svg width="12" height="12" viewBox="0 0 12 12"><circle cx="6" cy="6" r="5.2" fill="none" stroke="#fff" stroke-width="1"/><path d="M4 3.2 L5 4.6 L4.5 5.3 Q5.4 6.8 6.7 7.5 L7.4 7 L8.8 8 L8.2 8.9 Q5 8.6 3.2 4 Z" fill="#fff"/></svg>
        (816) 555.0187
      </p>
    </div>
    <div class="rule-gold"></div>
    <p class="barcode-label">Bar Code Area</p>
    <div class="edge-tick"></div>
  </section>
</div>
</body>
</html>
```